Business card for Delacroft Anesthesia LLC

This is for a business care for Delacroft Anesthesia LLC. Dr. Helen Delacroft, CRNA, DNAP is the sole provider in the LLC. Business address is 4716 N Brackley Avenue,
Larkfield, PA 19372
CRNA stands for certified registered nurse anesthetist
"Keeping you calm and cared for"
I plan to give this business card to the patients that I provide anesthesia to.
Creative design that ties into Anesthesia. Calm soothing colors.

Target Market(s)

Business card for my patients.

Industry/Entity Type

Medicine

Contact Information for Business Card

Creative, professional, eye catching

Logo Text

Delacroft Anesthesia

Font styles to use
Serif
Script

Colors

Designer to choose colors to be used in the design.

Requirements
Must have
• Delacroft Anesthesia
• Dr. Helen Delacroft, CRNA, DNAP
• delacroft.anesthesia@ quillmail.net
Nice to have
• "Keeping you calm and cared for"
Should not have
• phone number

```html
<!DOCTYPE html>
<html lang="en">
<head>
<meta charset="utf-8">
<title>Delacroft Anesthesia LLC – Business Card</title>
<link href="https://fonts.googleapis.com/css2?family=Source+Sans+3:wght@400;600&family=Parisienne&display=swap" rel="stylesheet">
<style>
  :root {
    --navy: #233a5e;
    --red: #dc2238;
    --white: #ffffff;
    --ink: #2a3a57;
    --stage: #2b2d31;
  }
  * { box-sizing: border-box; margin: 0; padding: 0; }
  html, body { width: 1200px; height: 900px; overflow: hidden; }
  body {
    background: var(--stage);
    font-family: "Source Sans 3", "Myriad Pro", Arial, sans-serif;
    position: relative;
  }
  .card {
    position: absolute;
    width: 525px;
    height: 300px;
    border-radius: 26px;
    overflow: hidden;
    top: 270px;
  }
  .card-front { left: 50px; background: var(--white); }
  .card-back { left: 625px; background: var(--navy); }

  .card-waves { position: absolute; inset: 0; width: 100%; height: 100%; }

  .brand {
    position: absolute;
    color: var(--navy);
    font-weight: 400;
    text-transform: uppercase;
    line-height: 1;
  }
  .brand-name, .brand-sub { display: block; }

  .card-front .brand { left: 36px; top: 40px; }
  .card-front .brand-name { font-size: 40px; letter-spacing: 1px; }
  .card-front .brand-sub { font-size: 15px; letter-spacing: 5px; margin-top: 6px; }

  .contact { position: absolute; left: 270px; top: 130px; color: var(--ink); }
  .contact-name { font-size: 24px; font-weight: 600; color: var(--navy); }
  .contact-title { font-size: 13px; color: var(--red); margin: 2px 0 12px; }
  .contact-line { display: flex; align-items: flex-start; gap: 8px; font-size: 13.5px; line-height: 1.3; margin-bottom: 6px; }
  .contact-line svg { flex: none; margin-top: 2px; }

  .card-back .brand {
    color: var(--white);
    left: 0; right: 0; top: 95px;
    text-align: center;
  }
  .card-back .brand-name { font-size: 50px; letter-spacing: 2px; }
  .card-back .brand-sub { font-size: 17px; letter-spacing: 7px; margin-top: 8px; }
  .tagline {
    position: absolute;
    left: 0; right: 0; top: 200px;
    text-align: center;
    color: var(--white);
    font-family: "Parisienne", cursive;
    font-size: 24px;
  }

  .lockup {
    position: absolute;
    right: 70px; bottom: 70px;
    color: var(--white);
    text-transform: uppercase;
    text-align: center;
    line-height: 1;
  }
  .lockup .brand-name { font-size: 46px; letter-spacing: 2px; }
  .lockup .brand-sub { font-size: 16px; letter-spacing: 6px; margin-top: 8px; }
</style>
</head>
<body>

  <section class="card card-front">
    <svg class="card-waves" viewBox="0 0 525 300" preserveAspectRatio="none" aria-hidden="true">
      <path d="M0 150 C 90 175, 190 225, 290 300 L 0 300 Z" fill="var(--navy)"/>
      <path d="M0 175 C 110 195, 200 240, 270 300 L 0 300 Z" fill="var(--white)"/>
      <path d="M0 190 C 120 215, 220 255, 300 300 L 0 300 Z" fill="var(--red)"/>
    </svg>

    <div class="brand">
      <span class="brand-name">Delacroft</span>
      <span class="brand-sub">Anesthesia LLC</span>
    </div>

    <div class="contact">
      <p class="contact-name">Helen Delacroft</p>
      <p class="contact-title">CRNA, DNAP</p>
      <p class="contact-line">
        <svg width="12" height="10" viewBox="0 0 12 10" aria-hidden="true"><rect width="12" height="10" rx="1" fill="var(--red)"/><path d="M1 1.5 6 5.5 11 1.5" stroke="#fff" stroke-width="1.2" fill="none"/></svg>
        <span>delacroft.anesthesia@ quillmail.net</span>
      </p>
      <p class="contact-line">
        <svg width="12" height="14" viewBox="0 0 12 14" aria-hidden="true"><path d="M6 0a5 5 0 0 1 5 5c0 4-5 9-5 9S1 9 1 5a5 5 0 0 1 5-5z" fill="var(--red)"/><circle cx="6" cy="5" r="1.8" fill="#fff"/></svg>
        <span>4716 N Brackley Avenue,<br>Larkfield, PA 19372</span>
      </p>
    </div>
  </section>

  <section class="card card-back">
    <div class="brand">
      <span class="brand-name">Delacroft</span>
      <span class="brand-sub">Anesthesia LLC</span>
    </div>
    <p class="tagline">Keeping you calm and cared for</p>
  </section>

  <div class="lockup">
    <span class="brand-name">Delacroft</span>
    <span class="brand-sub">Anesthesia LLC</span>
  </div>

</body>
</html>
```